Medical Cannabis Network Website

Need a informative, detailed and functional website for a medical cannabis clinic website

check out www.velmorahealthpoint.example as competition - want better site than they have

Target Market(s)

Patients

Industry/Entity Type

Health Care

Number of Pages Required

1 page

Font styles to use
Sans Serif

Colors
cadf82
abd036
9bcb3b
3276b5
33a6d7
0392cd
f68d4e

Requirements
Must have
• Clean / Informative
• Will add additional educational content on opioid reduction
Nice to have
• like the white contrast with black/slate dividers. Green logo looks good on slate
• Check documents for ppt regarding website ideas
Should not have
• too many words

```html
<!DOCTYPE html>
<html lang="en">
<head>
<meta charset="utf-8">
<title>Ridgeline Care Clinic</title>
<link href="https://fonts.googleapis.com/css2?family=Montserrat:wght@400;500;600;700&family=Open+Sans:wght@400;600&display=swap" rel="stylesheet">
<style>
  :root {
    --green: #6bb245;
    --green-dark: #4c9a3a;
    --green-card1: #6aa13f;
    --green-card2: #4fbf6e;
    --green-card3: #94c12b;
    --lime: #9bc12a;
    --lime-light: #abd036;
    --ink: #1d1d1d;
    --text: #3a3a3a;
    --white: #ffffff;
    --shadow: 0 1px 5px rgba(0,0,0,.14);
  }
  * { box-sizing: border-box; margin: 0; padding: 0; }
  html, body { width: 678px; height: 1200px; overflow: hidden; background: var(--white); }
  body { font-family: "Open Sans", Arial, sans-serif; color: var(--text); }
  .page { position: relative; width: 678px; height: 1200px; }

  /* top bar */
  .topbar { height: 13px; background: var(--green); display: flex; align-items: center; justify-content: space-between; padding: 0 132px; font-size: 4.5px; color: var(--white); }
  .topbar .contact { display: flex; gap: 10px; }
  .topbar .social { display: flex; gap: 7px; }
  .topbar .social span { width: 5px; height: 5px; border-radius: 50%; background: var(--white); }

  /* header */
  .header { height: 54px; display: flex; align-items: center; justify-content: space-between; padding: 0 132px 0 133px; }
  .brand { display: flex; align-items: center; gap: 6px; }
  .brand-mark { width: 12px; height: 12px; border-radius: 50%; background: var(--green); }
  .brand-name { font-family: "Montserrat", Arial, sans-serif; font-weight: 600; font-size: 10px; color: var(--green-dark); white-space: nowrap; }
  .nav { display: flex; gap: 18px; font-family: "Montserrat", Arial, sans-serif; font-size: 5.4px; font-weight: 600; color: var(--ink); }
  .nav .active { color: var(--green-dark); }

  /* hero */
  .hero { position: relative; height: 214px; }
  .hero-photo { position: absolute; inset: 0; background: linear-gradient(100deg, #3e5a26 0%, #6f8f3c 35%, #90a85a 55%, #cfd3c8 72%, #6c8a3e 100%); }
  .hero-title { position: absolute; left: 133px; top: 62px; width: 296px; height: 30px; background: #111; color: var(--white); font-family: "Montserrat", Arial, sans-serif; font-weight: 700; font-size: 17px; display: flex; align-items: center; justify-content: center; letter-spacing: .2px; }
  .hero-btn { position: absolute; left: 132px; top: 103px; width: 132px; height: 28px; background: var(--green); color: var(--white); font-family: "Montserrat", Arial, sans-serif; font-weight: 700; font-size: 8px; display: flex; align-items: center; justify-content: center; }
  .hero-arrow { position: absolute; top: 111px; }
  .hero-arrow.prev { left: 32px; }
  .hero-arrow.next { right: 32px; }

  /* feature cards */
  .features { position: absolute; top: 249px; left: 133px; display: flex; gap: 11px; }
  .feature { position: relative; width: 131px; height: 95px; color: var(--white); text-align: center; padding-top: 20px; border-radius: 2px; }
  .feature.risk { background: var(--green-card1); }
  .feature.faq { background: var(--green-card2); }
  .feature.opioid { background: var(--green-card3); }
  .feature-icon { position: absolute; left: 50%; top: -16px; width: 30px; height: 30px; margin-left: -15px; border-radius: 50%; background: inherit; display: flex; align-items: center; justify-content: center; }
  .feature h3 { font-family: "Montserrat", Arial, sans-serif; font-size: 8px; font-weight: 700; margin-bottom: 5px; }
  .feature p { font-size: 4.6px; line-height: 1.75; padding: 0 10px; }
  .feature .btn { display: inline-block; margin-top: 9px; width: 60px; height: 18px; line-height: 18px; font-size: 4.8px; background: rgba(0,0,0,.16); }

  /* welcome */
  .welcome { position: absolute; top: 375px; left: 0; width: 678px; text-align: center; }
  .welcome .eyebrow { font-family: "Montserrat", Arial, sans-serif; font-size: 4.6px; color: var(--ink); }
  .welcome h1 { font-family: "Montserrat", Arial, sans-serif; font-weight: 400; color: var(--green-dark); font-size: 13px; letter-spacing: 2.4px; margin-top: 6px; line-height: 1; }
  .welcome h2 { font-family: "Montserrat", Arial, sans-serif; font-weight: 400; color: var(--green); font-size: 8.6px; letter-spacing: 2.4px; margin-top: 7px; }
  .divider { display: flex; align-items: center; justify-content: center; gap: 6px; margin-top: 9px; }
  .divider i { width: 36px; height: 1px; background: var(--lime-light); }
  .divider b { width: 8px; height: 8px; border-radius: 50%; background: var(--green); }
  .welcome .copy { width: 296px; margin: 13px auto 0; font-size: 4.9px; line-height: 2.05; color: var(--ink); }
  .welcome .copy + .copy { margin-top: 10px; }
  .pill { display: inline-block; border-radius: 10px; color: var(--white); font-family: "Montserrat", Arial, sans-serif; font-weight: 700; font-size: 4.4px; }
  .welcome .pill { margin-top: 14px; width: 80px; height: 16px; line-height: 16px; background: var(--green); }

  /* steps */
  .steps-title { position: absolute; top: 601px; width: 678px; text-align: center; font-family: "Montserrat", Arial, sans-serif; font-weight: 600; font-size: 11px; color: var(--ink); }
  .steps { position: absolute; top: 638px; left: 133px; display: flex; gap: 11px; }
  .step { width: 131px; height: 146px; background: var(--white); box-shadow: var(--shadow); border-bottom: 2px solid var(--green); text-align: center; padding-top: 15px; }
  .step-icon { width: 35px; height: 35px; border-radius: 50%; margin: 0 auto; display: flex; align-items: center; justify-content: center; }
  .step h3 { font-family: "Montserrat", Arial, sans-serif; font-weight: 600; font-size: 6.4px; margin-top: 14px; }
  .step p { font-size: 4.6px; line-height: 1.95; padding: 0 14px; margin-top: 5px; color: var(--ink); }
  .step .pill { margin-top: 7px; width: 80px; height: 16px; line-height: 16px; }
  .step.doctor .step-icon, .step.doctor .pill { background: var(--green); }
  .step.doctor h3 { color: var(--green); }
  .step.apply .step-icon, .step.apply .pill { background: var(--green-card2); }
  .step.apply h3 { color: var(--green-card2); }
  .step.follow .step-icon, .step.follow .pill { background: var(--green-card3); }
  .step.follow h3 { color: var(--green-card3); }
  .step-arrow { position: absolute; top: 22px; }

  /* help & newsletter */
  .band { position: absolute; top: 818px; left: 0; width: 678px; height: 172px; display: flex; color: var(--white); }
  .help { width: 339px; background: var(--green); padding: 32px 0 0 31px; }
  .newsletter { width: 339px; background: var(--lime); padding: 32px 0 0 32px; }
  .band h2 { font-family: "Open Sans", Arial, sans-serif; font-weight: 600; font-size: 21px; line-height: 1; }
  .help .email { margin-top: 12px; font-size: 10px; padding-left: 2px; }
  .help .email strong, .help .phone strong { font-weight: 600; }
  .help hr { width: 270px; border: 0; border-top: 1px solid rgba(255,255,255,.35); margin: 15px 0 15px 2px; }
  .help .phone, .help .hours { font-size: 10px; padding-left: 2px; line-height: 1.6; }
  .newsletter p { margin-top: 10px; width: 270px; font-size: 6.3px; line-height: 1.55; }
  .signup { margin-top: 14px; width: 277px; height: 32px; border-radius: 16px; background: var(--white); display: flex; align-items: center; justify-content: space-between; padding: 0 8px 0 15px; font-size: 6px; color: var(--ink); }

  /* footer */
  .footer { position: absolute; top: 1040px; width: 678px; text-align: center; }
  .footer .brand { justify-content: center; height: 30px; }
  .footer-links { margin-top: 17px; display: flex; justify-content: center; gap: 12px; font-size: 4.8px; color: var(--ink); }
  .footer-links a { color: inherit; text-decoration: underline; }
  .copyright { margin-top: 17px; font-size: 4.8px; color: var(--ink); }
  .footer-social { margin-top: 24px; display: flex; justify-content: center; gap: 28px; }
  .footer-social span { width: 13px; height: 13px; border-radius: 50%; background: var(--green); }
</style>
</head>
<body>
<div class="page">

  <div class="topbar">
    <div class="contact">
      <span>&#9742; (555) 014-7890</span>
      <span>&#9993; info@ridgelinecare.example</span>
    </div>
    <div class="social"><span></span><span></span><span></span><span></span><span></span></div>
  </div>

  <header class="header">
    <div class="brand">
      <span class="brand-mark"></span>
      <div class="brand-name">Ridgeline Care</div>
    </div>
    <nav class="nav">
      <span class="active">HOME</span><span>ABOUT</span><span>QUALIFY</span><span>APPOINTMENTS</span><span>FAQ</span><span>CONTACT</span><span>NEWS</span>
    </nav>
  </header>

  <section class="hero">
    <div class="hero-photo" role="img" aria-label="Doctor in a white coat reviewing notes among cannabis plants"></div>
    <div class="hero-title">NOW TAKING APPOINTMENTS</div>
    <div class="hero-btn">BOOK APPOINTMENT</div>
    <svg class="hero-arrow prev" width="10" height="16" viewBox="0 0 10 16"><path d="M8 1 2 8l6 7" fill="none" stroke="#fff" stroke-width="1.6"/></svg>
    <svg class="hero-arrow next" width="10" height="16" viewBox="0 0 10 16"><path d="M2 1l6 7-6 7" fill="none" stroke="#fff" stroke-width="1.6"/></svg>
  </section>

  <div class="features">
    <div class="feature risk">
      <div class="feature-icon"><svg width="12" height="12"><circle cx="6" cy="6" r="5" fill="#fff"/></svg></div>
      <h3>100% RISK FREE</h3>
      <p>Speak with a licensed doctor first. If you do not qualify, your visit costs you nothing at all.</p>
      <span class="btn">Book Online</span>
    </div>
    <div class="feature faq">
      <div class="feature-icon"><svg width="14" height="13" viewBox="0 0 14 13"><path d="M1 1h12v8H6l-3 3V9H1z" fill="none" stroke="#fff" stroke-width="1.2"/><text x="7" y="7.5" font-size="6" fill="#fff" text-anchor="middle" font-family="Arial">?</text></svg></div>
      <h3>FAQ</h3>
      <p>Clear answers on eligibility, visits, card fees and what to bring to your first appointment.</p>
      <span class="btn">Read More</span>
    </div>
    <div class="feature opioid">
      <div class="feature-icon"><svg width="12" height="14" viewBox="0 0 12 14"><rect x="2" y="1" width="8" height="3" fill="none" stroke="#fff" stroke-width="1.1"/><rect x="1" y="4" width="10" height="9" rx="1" fill="none" stroke="#fff" stroke-width="1.1"/><path d="M6 6.5v4M4 8.5h4" stroke="#fff" stroke-width="1.1"/></svg></div>
      <h3>OPIOID REDUCTION</h3>
      <p>Learn how a guided care plan may help patients lower their reliance on opioid pain medicine.</p>
      <span class="btn">Read More</span>
    </div>
  </div>

  <section class="welcome">
    <div class="eyebrow">WELCOME TO</div>
    <h1>RIDGELINE CARE</h1>
    <h2>MEDICAL CLINIC</h2>
    <div class="divider"><i></i><b></b><i></i></div>
    <p class="copy">Our clinic helps qualifying patients get safe, legal access to medical cannabis. Every visit is with a caring, licensed physician who listens to your history, reviews your records and explains each step of the process, so you always know what comes next and feel at ease from your very first call.</p>
    <p class="copy">We keep things simple: book online, meet your doctor, apply for your card and come back for follow-up care. Our friendly team is here to answer questions, support your treatment goals and help you feel confident about your health, with clear advice and honest guidance at every single stage.</p>
    <span class="pill">READ MORE DETAILS</span>
  </section>

  <h2 class="steps-title">3 Steps to Get Your Arkansas Mediccal Card</h2>
  <div class="steps">
    <div class="step doctor">
      <div class="step-icon"><svg width="16" height="16" viewBox="0 0 16 16"><path d="M3 8.5l3.5 3.5L13 4.5" fill="none" stroke="#fff" stroke-width="1.6"/></svg></div>
      <h3>Meet a Arkansas Doctor</h3>
      <p>Book a short visit with a licensed doctor who will review your needs and history.</p>
      <span class="pill">BOOK AN APPOINTMENT</span>
    </div>
    <div class="step apply">
      <div class="step-icon"><svg width="17" height="13" viewBox="0 0 17 13"><rect x="1" y="1" width="15" height="11" rx="1" fill="none" stroke="#fff" stroke-width="1.1"/><rect x="3" y="4" width="4" height="5" fill="none" stroke="#fff" stroke-width="1"/><path d="M9 5h5M9 7h5M9 9h3" stroke="#fff" stroke-width="1"/></svg></div>
      <h3>Apply for Arkansas Card</h3>
      <p>Send your signed form and ID to the state health office to request your card.</p>
      <span class="pill">APPLY ONLINE AT ADH</span>
    </div>
    <div class="step follow">
      <div class="step-icon"><svg width="15" height="15" viewBox="0 0 15 15"><rect x="1" y="2" width="13" height="12" rx="1" fill="none" stroke="#fff" stroke-width="1.1"/><path d="M1 5.5h13M4 1v2.5M11 1v2.5M4 8h3M4 10.5h6" stroke="#fff" stroke-width="1"/></svg></div>
      <h3>Follow-up Appointment</h3>
      <p>Return for a check-in so your doctor can track progress and adjust your plan.</p>
      <span class="pill">BOOK FOLLOW UP</span>
    </div>
    <svg class="step-arrow" style="left:112px" width="56" height="20" viewBox="0 0 56 20"><path d="M2 16C14 2 38 0 52 12" fill="none" stroke="#a8a8a8" stroke-width="2.2"/><path d="M45 11l8 2-2-8" fill="none" stroke="#a8a8a8" stroke-width="2.2"/></svg>
    <svg class="step-arrow" style="left:254px" width="56" height="20" viewBox="0 0 56 20"><path d="M2 16C14 2 38 0 52 12" fill="none" stroke="#a8a8a8" stroke-width="2.2"/><path d="M45 11l8 2-2-8" fill="none" stroke="#a8a8a8" stroke-width="2.2"/></svg>
  </div>

  <section class="band">
    <div class="help">
      <h2>Need help?</h2>
      <div class="email">Email : <strong>contact@ridgelinecare.example</strong></div>
      <hr>
      <div class="phone"><strong>Phone : +1 555 014 2290</strong></div>
      <div class="hours">Monday - Saturday 9:00 - 18:00 hrs.</div>
    </div>
    <div class="newsletter">
      <h2>Newsletter Signup</h2>
      <p>Please subscribe and receive our latest news, promotions, events, and clinic updates you can't get anywhere else.</p>
      <div class="signup">
        <span>Type your email here</span>
        <svg width="17" height="17" viewBox="0 0 17 17"><circle cx="8.5" cy="8.5" r="8" fill="#6bb245"/><path d="M4 7h5V4.5l4 4-4 4V10H4z" fill="#fff"/></svg>
      </div>
    </div>
  </section>

  <footer class="footer">
    <div class="brand">
      <span class="brand-mark"></span>
      <div class="brand-name">Ridgeline Care</div>
    </div>
    <div class="footer-links"><a>Privacy</a><a>Terms of Use</a><a>Join Our Team</a></div>
    <div class="copyright">Copyright © 2019 Ridgeline Care Clinic. All Rights Reserved.</div>
    <div class="footer-social"><span></span><span></span><span></span><span></span><span></span></div>
  </footer>

</div>
</body>
</html>
```